Process Roadmap for Interior Design Firm

We are looking to ramp up the design appeal of our current process roadmap to be very visually interesting, while staying informative and descriptive about our process.

Target Market(s)

In-house Clients

Industry/Entity Type

Interior Design Firm focused on sustainable and holistic design.

Other font styles liked:
• raleway

Requirements
Must have
• 1.) it would be nice if the graphic provided a more clear indication of the “journey” from one step to the next, so that there was a clear sense of the progression (such that we are directing the viewer) 2.). We would want it to fit on an 8.5”x11” page (the page could be horizontal when we have the Calm Compass formatted out with the testimonials) (in addition to the testimonials, we may also want to have the detailed descriptions of each step of the process presented below the graphic, so that the graphic is cleaner) 3.) ideally the graphic is clear and simple enough to also be used on our Bi-Weekly Client Updates, which will be typed updates for clients re their project budgets, schedule and scope. The Calm Compass graphic (without all the testimonials) would be at the end of the update, and would fit on the page horizontally at the bottom, perhaps in a space which is 7.5”w x 4”h or so.
Should not have
• bold or bright colors. Natural neutrals are preferred, such as the ones featured on the provided graphic.

```html
<!DOCTYPE html>
<html lang="en">
<head>
<meta charset="utf-8">
<title>IHD Calm Compass</title>
<link rel="stylesheet" href="https://fonts.googleapis.com/css2?family=Raleway:wght@400;600;700&family=Playfair+Display:wght@700&display=swap">
<style>
:root{
  --frame:#c19c5a;
  --gold:#b8914a;
  --gold-soft:#d9c29a;
  --ink:#3b3834;
  --card:#ffffff;
  --band:#f3eee4;
  --badge:#e3d0aa;
  --quote:#eadfca;
  --corner:#f1e8d6;
}
*{box-sizing:border-box;margin:0;padding:0}
html,body{width:1200px;height:943px;overflow:hidden}
body{background:var(--frame);font-family:"Raleway",sans-serif;color:var(--ink);position:relative}
.card{position:absolute;left:124px;top:104px;width:952px;height:735px;
  background:linear-gradient(180deg,var(--card) 45%,#f9f6f0 100%);overflow:hidden}
.corner-block{position:absolute;left:124px;top:104px;width:50px;height:117px;background:var(--corner)}
.brand{position:absolute;left:202px;top:122px;font-family:"Raleway",sans-serif;font-weight:400;color:var(--gold);letter-spacing:.28em}
.brand span{display:block;line-height:1}
.brand .b1{font-size:16px}
.brand .b2{font-size:27px;margin-top:6px}
.brand .b3{font-size:16px;margin-top:6px;text-align:right;letter-spacing:.3em}
.title{position:absolute;left:421px;top:148px;font-weight:600;font-size:62px;color:var(--gold);letter-spacing:-.5px;white-space:nowrap}
.art{position:absolute;left:0;top:0}
.step-title{position:absolute;font-weight:700;font-size:15px;color:var(--gold)}
.point{position:absolute;font-size:9.4px;line-height:11.5px}
.point::before{content:"";position:absolute;left:-18px;top:50%;width:6px;height:6px;margin-top:-3px;border:1px solid var(--gold-soft);border-radius:50%}
.band{position:absolute;left:124px;top:665px;width:952px;height:174px;background:var(--band);border-top:1px solid var(--gold-soft)}
.band-title{position:absolute;left:153px;top:681px;font-weight:700;font-size:30px;color:var(--gold)}
.quote-mark{position:absolute;left:216px;top:690px;font-family:"Playfair Display",serif;font-size:220px;line-height:1;color:var(--quote)}
.badge{position:absolute;width:35px;height:35px;border-radius:50%;background:var(--badge);color:#fff;font-weight:700;font-style:normal;font-size:15px;display:flex;align-items:center;justify-content:center;top:742px}
.testimonial{position:absolute;top:727px;width:100px;font-size:10.8px;line-height:12.9px}
</style>
</head>
<body>
<div class="card"></div>
<div class="corner-block" role="img" aria-label="Decorative corner pattern area"></div>
<div class="brand"><span class="b1">IVY</span><span class="b2">HARLOW</span><span class="b3">DESIGN</span></div>
<h1 class="title">IHD Calm Compass</h1>

<svg class="art" width="1200" height="943" viewBox="0 0 1200 943">
  <defs>
    <linearGradient id="divider" x1="0" y1="0" x2="0" y2="1">
      <stop offset="0" stop-color="#d9c29a" stop-opacity="0"/>
      <stop offset="1" stop-color="#d9c29a" stop-opacity="1"/>
    </linearGradient>
    <filter id="soft" x="-30%" y="-30%" width="160%" height="160%">
      <feDropShadow dx="3" dy="4" stdDeviation="4" flood-color="#b8914a" flood-opacity=".18"/>
    </filter>
    <marker id="head" markerWidth="8" markerHeight="8" refX="5" refY="4" orient="auto">
      <path d="M0 0 L7 4 L0 8 L2 4 Z" fill="#b8914a"/>
    </marker>
  </defs>
  <g class="dividers">
    <rect x="278" y="370" width="1" height="295" fill="url(#divider)"/>
    <rect x="409" y="330" width="1" height="335" fill="url(#divider)"/>
    <rect x="534" y="320" width="1" height="345" fill="url(#divider)"/>
    <rect x="663" y="320" width="1" height="345" fill="url(#divider)"/>
    <rect x="791" y="350" width="1" height="315" fill="url(#divider)"/>
    <rect x="910" y="400" width="1" height="265" fill="url(#divider)"/>
  </g>
  <g fill="none" stroke="#b8914a" stroke-width="2">
    <path d="M124 505 Q150 480 174 459"/>
    <path d="M1009 464 Q1045 495 1076 530"/>
  </g>
  <g stroke="#b8914a" stroke-width="1.6" marker-end="url(#head)">
    <line x1="266" y1="398" x2="280" y2="386"/>
    <line x1="387" y1="342" x2="402" y2="335"/>
    <line x1="516" y1="312" x2="533" y2="310"/>
    <line x1="648" y1="309" x2="666" y2="313"/>
    <line x1="780" y1="335" x2="796" y2="343"/>
    <line x1="902" y1="386" x2="915" y2="399"/>
  </g>
  <g class="pins" fill="#fff" stroke="#c9a468" stroke-width="1.2" filter="url(#soft)">
    <path d="M208.2 465.3 A45 45 0 1 1 223.8 465.3 L216 475 Z"/>
    <path d="M324.2 401.3 A45 45 0 1 1 339.8 401.3 L332 411 Z"/>
    <path d="M451.2 360.3 A45 45 0 1 1 466.8 360.3 L459 370 Z"/>
    <path d="M584.2 347.3 A45 45 0 1 1 599.8 347.3 L592 357 Z"/>
    <path d="M716.2 362.3 A45 45 0 1 1 731.8 362.3 L724 372 Z"/>
    <path d="M843.2 403.3 A45 45 0 1 1 858.8 403.3 L851 413 Z"/>
    <path d="M960.2 469.3 A45 45 0 1 1 975.8 469.3 L968 479 Z"/>
  </g>
  <g class="icons" fill="#f2e9d8">
    <circle cx="216" cy="421" r="24" role="img" aria-label="Line icon of a speech bubble"/>
    <circle cx="332" cy="357" r="26" role="img" aria-label="Line icon of a house with an eye"/>
    <circle cx="459" cy="316" r="26" role="img" aria-label="Line icon of a clipboard checklist"/>
    <circle cx="592" cy="303" r="28" role="img" aria-label="Line icon of drafting tools and a light bulb"/>
    <circle cx="724" cy="318" r="28" role="img" aria-label="Line icon of a manager with budget and schedule symbols"/>
    <circle cx="851" cy="359" r="26" role="img" aria-label="Line icon of a gear with circular arrows"/>
    <circle cx="968" cy="425" r="26" role="img" aria-label="Line icon of a handshake"/>
  </g>
  <polyline fill="none" stroke="#d8c7a5" stroke-width="1" points="348,699 430,699 442,711 454,699 601,699 613,711 625,699 771,699 783,711 795,699 932,699 944,711 956,699 1004,699"/>
</svg>

<h2 class="step-title" style="left:181px;top:494px">Listening</h2>
<p class="point" style="left:184px;top:521px;width:72px">Listening to our clients, their land, and their home</p>
<p class="point" style="left:184px;top:584px;width:86px">Identifying their needs, challenges, wishes, and dreams</p>

<h2 class="step-title" style="left:302px;top:427px">Visioning</h2>
<p class="point" style="left:309px;top:458px;width:80px">Facilitating a guided visioning process to clarify the deepest intention, true purposes, and highest potential for their home and their future within it</p>

<h2 class="step-title" style="left:436px;top:391px">Planning</h2>
<p class="point" style="left:436px;top:420px;width:90px">Turning our client's vision into a clearly defined scope, budget, and timeline.</p>
<p class="point" style="left:436px;top:494px;width:80px">Mapping out the steps for making their dream a reality.</p>
<p class="point" style="left:436px;top:558px;width:82px">Setting a meeting schedule from start to finish.</p>

<h2 class="step-title" style="left:561px;top:378px">Designing</h2>
<p class="point" style="left:560px;top:414px;width:92px">Following the schedule through the design phases from initial design concepts, technical drawings and details, and the selection of all finishes, fixtures, and surnishings.</p>

<h2 class="step-title" style="left:687px;top:393px">Managing</h2>
<p class="point" style="left:690px;top:426px;width:89px">Cordinating with clients, builders, architects, and vendors to ensure that the design is executed with excellence, and the construction and furnishings are on-time and on-budget.</p>

<h2 class="step-title" style="left:805px;top:431px">Installing</h2>
<p class="point" style="left:816px;top:462px;width:84px">Overseeing the inspection, installation, and arrangement of all furnishings, lighting, artwork, and decorative items.</p>
<p class="point" style="left:816px;top:572px;width:64px">Taking care of every last detail.</p>

<h2 class="step-title" style="left:930px;top:497px">Completing</h2>
<p class="point" style="left:942px;top:525px;width:92px">Fixing any issues or defects.</p>
<p class="point" style="left:942px;top:560px;width:90px">Follow up on all remaining items.</p>
<p class="point" style="left:942px;top:595px;width:76px">Completing the final finishing touches to our client's full and total satisfaction.</p>

<div class="band"></div>
<h2 class="band-title">Testimonials</h2>
<div class="quote-mark" aria-hidden="true">&ldquo;</div>

<i class="badge" style="left:355px">1.</i>
<p class="testimonial" style="left:409px">Ivy to send over testimonials for fill this space - three or four columns of testimonials</p>
<i class="badge" style="left:524px">1.</i>
<p class="testimonial" style="left:578px">Ivy to send over testimonials for fill this space - three or four columns of testimonials</p>
<i class="badge" style="left:693px">1.</i>
<p class="testimonial" style="left:747px">Ivy to send over testimonials for fill this space - three or four columns of testimonials</p>
<i class="badge" style="left:862px">1.</i>
<p class="testimonial" style="left:916px">Ivy to send over testimonials for fill this space - three or four columns of testimonials</p>
</body>
</html>
```